AI Maple Sprint Presentation

We have a wireframe presentation with 43 slides (many with the same format) to be implemented in Powerpoint. We provide Corporate presentation in order to reuse template. Please, be creative and don't take the examples in the wireframe as literal. We also provide the following:
- Color palette
- lumafox Logos
- Slide wireframe
- Flyer
- lumafox Corporate Presentation. Please, use this as a general template.
You can find all the materials here:
https://files.brenvale.net/shared/7QpLxZ2RtK9mVwB4nYcHs0JdFgE3aUoT?view=link

```html
<!DOCTYPE html>
<html lang="en">
<head>
<meta charset="utf-8">
<title>AI Maple Sprint — Slide Set</title>
<link href="https://fonts.googleapis.com/css2?family=Poppins:wght@400;500;600;700;800&display=swap" rel="stylesheet">
<style>
:root{
  --stage:#7a7a7a;
  --navy:#08152a;
  --navy-2:#0c1f36;
  --teal:#17968b;
  --teal-soft:#3a8f86;
  --teal-bright:#1fb3a4;
  --purple:#730a74;
  --olive:#8f8a1f;
  --grey-tile:#6b6f72;
  --white:#ffffff;
  --muted:#cfd8e0;
}
*{box-sizing:border-box;margin:0;padding:0}
html,body{width:1067px;height:1200px;overflow:hidden;background:var(--stage);font-family:'Poppins',sans-serif;color:var(--white)}
.deck{position:relative;width:1067px;height:1200px}
.slide{position:absolute;width:445px;height:250px;overflow:hidden;
  background:
    radial-gradient(ellipse 60% 55% at 15% 95%, rgba(23,150,139,.55), transparent 70%),
    radial-gradient(ellipse 45% 50% at 95% 100%, rgba(115,10,116,.6), transparent 70%),
    var(--navy);
  box-shadow:0 6px 18px rgba(0,0,0,.45)}
.col-l{left:82px}.col-r{left:539px}
.row-1{top:85px}.row-2{top:345px}.row-3{top:605px}.row-4{top:865px}
.abs{position:absolute}
.brand{position:absolute;display:flex;align-items:center;gap:3px;font-weight:600;line-height:1;color:var(--white)}
.brand .mark{display:inline-block;background:var(--teal)}
.brand-footer{left:13px;top:227px;font-size:13px}
.brand-footer .mark{width:7px;height:7px}
.heading{position:absolute;left:35px;top:24px;display:flex;align-items:center;gap:5px;font-weight:700;font-size:19px;line-height:1}
.heading .mark{width:13px;height:13px;background:var(--teal)}
.page-no{position:absolute;left:431px;top:237px;width:9px;height:8px;background:var(--purple);font-size:4px;font-weight:600;display:flex;align-items:center;justify-content:center}
.photo{position:absolute;border-radius:50%}
.teal{color:var(--teal-bright)}
/* title slide */
.title-main{left:40px;top:108px;font-size:19px;font-weight:700;line-height:1.3}
.template-by{left:40px;top:173px;font-size:7.5px;font-weight:700}
.title-note{left:40px;top:196px;font-size:7.5px;line-height:1.45;width:170px}
/* agenda */
.stage-step{position:absolute;top:90px;width:80px;height:80px;border-radius:50%;border:3px solid var(--teal);background:var(--navy);display:flex;flex-direction:column;align-items:center;justify-content:center;font-size:10px;line-height:1.5}
.stage-step b{font-weight:700;font-size:12px}
.stage-step.is-current{background:var(--teal);border-color:var(--navy-2)}
.arrow{position:absolute;top:126px}
/* intro */
.profile-card{left:35px;top:62px;width:150px;height:140px;border:1px solid #24405a;padding:4px}
.profile-card .inner{border:1px solid #41607a;height:100%;padding:14px 0 0 19px;font-size:7px;line-height:1}
.profile-card .name{font-weight:700;font-size:8px;margin-bottom:9px}
.profile-card p{margin-bottom:8px}
.profile-card .label{color:var(--teal-bright);font-weight:700;font-size:6.5px;margin:3px 0 7px}
.profile-card .expect{font-size:6px;line-height:1.9;width:118px}
.date-tag{left:60px;top:190px;width:69px;height:15px;background:var(--purple);font-size:6px;font-weight:600;display:flex;align-items:center;justify-content:center;gap:4px}
/* AI */
.ai-copy{left:227px;top:100px;font-size:11px;line-height:1.72;width:190px}
/* about */
.about-sub{left:54px;top:74px;font-size:14px;font-weight:700;line-height:1.6;color:var(--teal)}
.about-copy{left:54px;top:129px;font-size:8.2px;line-height:2.13;width:225px}
/* ML grid */
.tile{position:absolute;width:129px;height:65px;display:flex;align-items:center;justify-content:space-between;padding:0 14px 0 18px;font-size:7.5px;font-weight:700;line-height:1.5}
.tile svg{width:34px;height:34px;fill:none;stroke:var(--white);stroke-width:1.6}
.tile-demand{left:26px;top:70px;background:var(--teal-soft)}
.tile-reco{left:26px;top:138px;background:var(--purple)}
.tile-segment{left:158px;top:70px;height:133px;background:#0b1a2e;flex-direction:column;justify-content:center;gap:16px;text-align:center;padding:0}
.tile-segment svg{stroke:var(--teal-soft);width:44px;height:44px}
.tile-fraud{left:290px;top:70px;background:var(--olive)}
.tile-churn{left:290px;top:138px;background:var(--grey-tile)}
/* divider */
.divider-title{left:91px;top:103px;display:flex;align-items:center;gap:8px;font-size:30px;font-weight:700;line-height:1}
.divider-title .mark{width:22px;height:22px;background:var(--teal)}
/* closing */
.closing-brand{left:258px;top:34px;font-size:26px}
.closing-brand .mark{width:12px;height:12px}
.closing-title{left:258px;top:95px;font-size:24px;font-weight:700;line-height:1.3}
.closing-thanks{left:258px;top:172px;font-size:19px;font-weight:700}
.office{position:absolute;top:210px;font-size:6.5px;line-height:1.7;padding-left:14px}
.office::before{content:"";position:absolute;left:0;top:3px;width:7px;height:5px;background:var(--teal)}
</style>
</head>
<body>
<main class="deck">

  <!-- Title -->
  <section class="slide col-l row-1">
    <div class="brand" style="left:40px;top:22px;font-size:26px"><span class="mark" style="width:12px;height:12px"></span>lumafox</div>
    <h1 class="abs title-main"><span class="teal">AI Maple</span><br>Sprint</h1>
    <p class="abs template-by">Template By:</p>
    <p class="abs title-note">Lorem Ipsum is simply dummy text of the printing and typesetting industry.</p>
    <div class="photo" role="img" aria-label="Presenter at an interactive screen in front of a seated audience" style="left:237px;top:90px;width:224px;height:224px;border:6px solid var(--navy-2);background:radial-gradient(circle at 45% 35%,#e9eef2,#aab7c2 55%,#4c5d6e)"></div>
  </section>

  <!-- Agenda -->
  <section class="slide col-r row-1" style="background:radial-gradient(ellipse 70% 60% at 50% 75%,rgba(23,150,139,.35),transparent 70%),radial-gradient(ellipse 40% 50% at 95% 95%,rgba(115,10,116,.65),transparent 70%),var(--navy)">
    <h2 class="heading"><span class="mark"></span>Agenda</h2>
    <div class="stage-step is-current" style="left:44px"><b>Inspire</b>(60 Minutes)</div>
    <svg class="arrow" style="left:138px" width="30" height="8" viewBox="0 0 30 8"><path d="M0 4H28M24 1l4 3-4 3" stroke="#fff" stroke-width="1" fill="none"/></svg>
    <div class="stage-step" style="left:183px"><b>Discover</b>(60 Minutes)</div>
    <svg class="arrow" style="left:277px" width="30" height="8" viewBox="0 0 30 8"><path d="M0 4H28M24 1l4 3-4 3" stroke="#fff" stroke-width="1" fill="none"/></svg>
    <div class="stage-step" style="left:322px"><b>Prioritize</b>(90 Minutes)</div>
    <div class="brand brand-footer"><span class="mark"></span>lumafox</div>
    <div class="page-no">05</div>
  </section>

  <!-- Introduction -->
  <section class="slide col-l row-2">
    <h2 class="heading"><span class="mark"></span>Introduction</h2>
    <div class="abs" role="img" aria-label="Teal tinted technology imagery panel" style="left:373px;top:0;width:72px;height:250px;background:linear-gradient(180deg,#127a72,#0d5a57 60%,#3a1250)"></div>
    <div class="abs profile-card">
      <div class="inner">
        <p class="name">Marta Velasco</p>
        <p>Lorem Ipsum</p>
        <p>Rol : lorem ipsum dolor sit</p>
        <p class="label">WORKSHOP EXPECTATIONS</p>
        <p class="expect">Sed ut perspiciatis unde omnis iste natus error sit voluptatem cusantium doloremque laudantium</p>
      </div>
    </div>
    <div class="abs date-tag"><svg width="6" height="6" viewBox="0 0 6 6"><rect x="0" y="1" width="6" height="5" fill="#fff"/></svg>Aug 02,2025</div>
    <div class="photo" role="img" aria-label="Portrait of the smiling workshop host in a dark blazer" style="left:250px;top:64px;width:158px;height:158px;border:5px solid var(--navy-2);background:radial-gradient(circle at 50% 40%,#e6e9e8,#9aa4a2 55%,#2a3138)"></div>
    <div class="brand brand-footer"><span class="mark"></span>lumafox</div>
    <div class="page-no">02</div>
  </section>

  <!-- Artificial Intelligence -->
  <section class="slide col-r row-2">
    <h2 class="heading"><span class="mark"></span>Artificial Intelligence</h2>
    <div class="abs" role="img" aria-label="Glowing blue hands holding a circuit chip marked AI" style="left:0;top:55px;width:215px;height:175px;background:radial-gradient(ellipse 55% 55% at 52% 50%,rgba(40,150,230,.75),rgba(20,80,160,.35) 55%,transparent 80%)"></div>
    <p class="abs ai-copy">It is the general field of computer science dedicated to creating machines that can simulate human intelligence</p>
    <div class="brand brand-footer"><span class="mark"></span>lumafox</div>
    <div class="page-no">06</div>
  </section>

  <!-- About Us -->
  <section class="slide col-l row-3">
    <div class="abs" role="img" aria-label="Profile of a woman in glasses with glowing data overlays" style="left:250px;top:0;width:195px;height:250px;background:radial-gradient(ellipse 60% 70% at 65% 40%,rgba(120,150,180,.45),rgba(40,60,90,.3) 55%,transparent 80%),linear-gradient(200deg,transparent 50%,rgba(115,10,116,.5))"></div>
    <h2 class="heading"><span class="mark"></span>About Us</h2>
    <p class="abs about-sub">Data Analytics &amp;<br>AI for Nonconformists</p>
    <p class="abs about-copy">We are a leading Professional Services company specialized in the design and implementation of cutting edge technologies in Cloud, Data Analytics &amp; AI.</p>
    <div class="brand brand-footer"><span class="mark"></span>lumafox</div>
    <div class="page-no">03</div>
  </section>

  <!-- ML Examples -->
  <section class="slide col-r row-3" style="background:radial-gradient(ellipse 70% 40% at 50% 95%,rgba(40,90,150,.45),transparent 70%),var(--navy)">
    <h2 class="heading"><span class="mark"></span>ML Examples</h2>
    <div class="tile tile-demand"><span>Demand<br>Prediction</span>
      <svg viewBox="0 0 34 34"><rect x="8" y="22" width="4" height="9"/><rect x="15" y="18" width="4" height="13"/><rect x="22" y="14" width="4" height="17"/><path d="M4 18L14 10l6 4 10-9M26 5h4v4"/></svg></div>
    <div class="tile tile-reco"><svg viewBox="0 0 34 34"><rect x="8" y="4" width="20" height="14"/><path d="M11 9h14M11 13h9"/><rect x="18" y="21" width="10" height="9"/><path d="M4 30v-8h6v8z"/></svg><span>Recommendation<br>Engine</span></div>
    <div class="tile tile-segment"><span>Customer<br>Segmentation</span>
      <svg viewBox="0 0 44 44"><circle cx="22" cy="24" r="12"/><rect x="17" y="24" width="3" height="6"/><rect x="22" y="20" width="3" height="10"/><circle cx="8" cy="8" r="3"/><circle cx="36" cy="8" r="3"/><circle cx="8" cy="38" r="3"/><circle cx="36" cy="38" r="3"/></svg></div>
    <div class="tile tile-fraud"><svg viewBox="0 0 34 34"><circle cx="15" cy="14" r="8"/><path d="M21 20l7 7M15 10v5M15 17v1"/></svg><span style="width:52px">Fraud<br>detection</span></div>
    <div class="tile tile-churn"><span>Employee<br>attrition/churn</span>
      <svg viewBox="0 0 34 34"><circle cx="17" cy="10" r="5"/><circle cx="8" cy="20" r="3.5"/><circle cx="26" cy="20" r="3.5"/><path d="M2 31c0-4 3-6 6-6s6 2 6 6M20 31c0-4 3-6 6-6s6 2 6 6"/></svg></div>
    <div class="brand brand-footer"><span class="mark"></span>lumafox</div>
    <div class="page-no">07</div>
  </section>

  <!-- Section Divider -->
  <section class="slide col-l row-4">
    <h2 class="abs divider-title"><span class="mark"></span>Section Divider</h2>
    <div class="brand brand-footer"><span class="mark"></span>lumafox</div>
    <div class="page-no">04</div>
  </section>

  <!-- Closing -->
  <section class="slide col-r row-4">
    <div class="photo" role="img" aria-label="Humanoid robot head linked to glowing neural network fibres" style="left:1px;top:92px;width:224px;height:224px;background:radial-gradient(circle at 70% 45%,#6fa8d8,#2b4f7a 40%,#10213a 70%),var(--navy-2)"></div>
    <div class="brand closing-brand"><span class="mark"></span>lumafox</div>
    <h2 class="abs closing-title"><span class="teal">We Are</span><br>Your Partner</h2>
    <p class="abs closing-thanks">Thank You</p>
    <p class="office" style="left:258px">Lisbon<br>Avenida Sol 24</p>
    <p class="office" style="left:337px">Porto<br>Rua Clara 57</p>
  </section>

</main>
</body>
</html>
```